Derek Hollins Business card

Hey there, I’m hoping to have a business card designed. I’m in Real estate and just switched to a new Brokerage called: The Property Quarter

The back could just be the company name maybe or whatever looks good!

I’ve attached some logos of our company and some cards my buddy had done up.

On the card:
Derek Hollins
derekhollins@mailbox-demo.com
587-214-6093
derekhollins-demo.ca

Target Market(s)

Home buyers and sellers

Industry/Entity Type

Real Estate

Contact Information for Business Card

just looking for a cool and modern design with my picture on it. I like the idea of Black and red being used.

Requirements
Must have
• all the details provided. I'm open to anything. Just want a professional looking card.

```html
<!DOCTYPE html>
<html lang="en">
<head>
<meta charset="utf-8">
<title>Derek Hollins – Business Card</title>
<link rel="stylesheet" href="https://fonts.googleapis.com/css2?family=Poppins:wght@300;400&family=Montserrat:wght@800&display=swap">
<style>
  :root {
    --bg: #2a2a2a;
    --card: #0c0c0c;
    --red: #e0213f;
    --white: #f4f4f4;
    --photo-dark: #1d2229;
    --photo-light: #5b5450;
  }
  * { box-sizing: border-box; margin: 0; padding: 0; }
  html, body { width: 1200px; height: 900px; overflow: hidden; }
  body {
    background: var(--bg);
    display: flex;
    align-items: center;
    justify-content: center;
    gap: 40px;
    font-family: "Poppins", sans-serif;
  }
  .card {
    position: relative;
    width: 540px;
    height: 309px;
    background: var(--card);
    border-radius: 18px;
    border-bottom: 5px solid var(--red);
    overflow: hidden;
    box-shadow: 0 12px 30px rgba(0,0,0,.45);
  }
  .card-front .portrait {
    position: absolute;
    left: 40px;
    bottom: 0;
    width: 200px;
    height: 250px;
    background: linear-gradient(180deg, var(--photo-light) 0%, var(--photo-dark) 75%);
    border-radius: 100px 100px 0 0;
  }
  .card-front .details {
    position: absolute;
    left: 262px;
    top: 88px;
  }
  .agent-name {
    color: var(--red);
    font-weight: 400;
    font-size: 27px;
    letter-spacing: 1px;
    text-transform: uppercase;
    line-height: 1;
  }
  .name-rule {
    width: 30px;
    height: 2px;
    background: var(--red);
    margin: 18px 0 16px 12px;
  }
  .contact-list { list-style: none; }
  .contact-list li {
    display: flex;
    align-items: center;
    gap: 10px;
    color: var(--white);
    font-size: 14px;
    font-weight: 300;
    line-height: 1;
    margin-bottom: 12px;
  }
  .contact-list svg { width: 16px; height: 16px; flex: none; }
  .card-back {
    display: flex;
    align-items: center;
    justify-content: center;
  }
  .brokerage-name {
    display: flex;
    align-items: center;
    gap: 12px;
    color: var(--white);
    font-family: "Montserrat", sans-serif;
    font-weight: 800;
    font-size: 30px;
    text-transform: uppercase;
    letter-spacing: 0.5px;
  }
  .brokerage-dot {
    width: 16px;
    height: 16px;
    border-radius: 50%;
    background: var(--red);
  }
</style>
</head>
<body>
  <section class="card card-front">
    <div class="portrait" role="img" aria-label="Portrait photo of Derek Hollins in a dark suit and white shirt"></div>
    <div class="details">
      <h1 class="agent-name">Derek Hollins</h1>
      <div class="name-rule"></div>
      <ul class="contact-list">
        <li>
          <svg viewBox="0 0 24 24" fill="none" stroke="var(--red)" stroke-width="2" stroke-linecap="round" stroke-linejoin="round"><path d="M22 16.9v3a2 2 0 0 1-2.2 2 19.8 19.8 0 0 1-8.6-3.1 19.5 19.5 0 0 1-6-6A19.8 19.8 0 0 1 2.1 4.2 2 2 0 0 1 4.1 2h3a2 2 0 0 1 2 1.7c.1 1 .4 1.9.7 2.8a2 2 0 0 1-.5 2.1L8 9.9a16 16 0 0 0 6 6l1.3-1.3a2 2 0 0 1 2.1-.4c.9.3 1.8.6 2.8.7a2 2 0 0 1 1.7 2z"/></svg>
          587-214-6093
        </li>
        <li>
          <svg viewBox="0 0 24 24" fill="var(--red)"><path d="M2 5h20v14H2z"/><path d="M2 5l10 8 10-8" fill="none" stroke="var(--card)" stroke-width="1.6"/></svg>
          derekhollins@mailbox-demo.com
        </li>
        <li>
          <svg viewBox="0 0 24 24" fill="none" stroke="var(--red)" stroke-width="1.8"><circle cx="12" cy="12" r="10"/><path d="M2 12h20M12 2c3 3 3 17 0 20M12 2c-3 3-3 17 0 20"/></svg>
          derekhollins-demo.ca
        </li>
      </ul>
    </div>
  </section>

  <section class="card card-back">
    <div class="brokerage-name">
      <span class="brokerage-dot"></span>
      The Property Quarter
    </div>
  </section>
</body>
</html>
```